Real eatate

My company name is “Silver Heron Realestate” i would like to create a business card. I would like something modern and sleek similar to picture uploaded. All text in the business card should be black and the logo gold any shade.

```html
<!DOCTYPE html>
<html lang="en">
<head>
<meta charset="UTF-8">
<title>Silver Heron Realestate – Business Card</title>
<link href="https://fonts.googleapis.com/css2?family=Work+Sans:wght@400;500;600&display=swap" rel="stylesheet">
<style>
  :root {
    --stage: #1c1c1c;
    --card: #f6f4ef;
    --ink: #111111;
    --gold: #c9973a;
  }
  * { margin: 0; padding: 0; box-sizing: border-box; }
  html, body {
    width: 1200px;
    height: 900px;
    overflow: hidden;
    background: var(--stage);
    font-family: "Work Sans", Arial, sans-serif;
  }
  .canvas {
    position: relative;
    width: 1200px;
    height: 900px;
    display: flex;
    flex-direction: column;
    align-items: center;
    justify-content: center;
    gap: 24px;
  }
  .card {
    position: relative;
    width: 700px;
    height: 400px;
    background: var(--card);
    border-radius: 3px;
    box-shadow: 0 10px 30px rgba(0,0,0,0.55);
  }

  /* Brand name block (gold) */
  .brand {
    display: flex;
    align-items: center;
    gap: 14px;
    color: var(--gold);
    font-weight: 600;
  }
  .brand-dot {
    width: 18px;
    height: 18px;
    border-radius: 50%;
    background: var(--gold);
    flex-shrink: 0;
  }
  .brand-name {
    text-transform: uppercase;
    line-height: 1.15;
  }
  .brand-name .line-main { display: block; letter-spacing: 1px; }
  .brand-name .line-sub { display: block; }

  /* Front */
  .card-front .brand {
    position: absolute;
    left: 50%;
    top: 50%;
    transform: translate(-50%, -50%);
  }
  .card-front .brand-name { font-size: 34px; }
  .card-front .brand-name .line-sub { font-size: 20px; letter-spacing: 12px; }

  /* Back */
  .card-back .brand {
    position: absolute;
    left: 52px;
    top: 50%;
    transform: translateY(-50%);
  }
  .card-back .brand-dot { width: 14px; height: 14px; }
  .card-back .brand-name { font-size: 26px; }
  .card-back .brand-name .line-sub { font-size: 15px; letter-spacing: 9.5px; }

  .divider {
    position: absolute;
    left: 375px;
    top: 95px;
    width: 2px;
    height: 205px;
    background: var(--ink);
  }

  .contact {
    position: absolute;
    left: 405px;
    top: 98px;
    color: var(--ink);
  }
  .contact-name {
    font-size: 27px;
    font-weight: 500;
    letter-spacing: 2px;
    text-transform: uppercase;
    line-height: 1.1;
  }
  .contact-role {
    font-size: 17px;
    margin-bottom: 14px;
  }
  .contact-address {
    font-size: 17px;
    line-height: 1.35;
    letter-spacing: 0.4px;
    margin-bottom: 4px;
  }
  .contact-line {
    display: flex;
    align-items: center;
    gap: 7px;
    font-size: 17px;
    line-height: 1.45;
    letter-spacing: 0.4px;
  }
  .contact-line svg {
    width: 12px;
    height: 12px;
    flex-shrink: 0;
  }
</style>
</head>
<body>
<main class="canvas">

  <section class="card card-front" aria-label="Business card front">
    <div class="brand">
      <span class="brand-dot"></span>
      <span class="brand-name">
        <span class="line-main">Silver Heron</span>
        <span class="line-sub">Realestate</span>
      </span>
    </div>
  </section>

  <section class="card card-back" aria-label="Business card back">
    <div class="brand">
      <span class="brand-dot"></span>
      <span class="brand-name">
        <span class="line-main">Silver Heron</span>
        <span class="line-sub">Realestate</span>
      </span>
    </div>

    <div class="divider"></div>

    <div class="contact">
      <p class="contact-name">Daniel Harper</p>
      <p class="contact-role">Founder</p>
      <p class="contact-address">418 Alder Lane<br>Colville, WA 99114</p>
      <p class="contact-line">
        <svg viewBox="0 0 24 24" aria-hidden="true"><path fill="currentColor" d="M6.6 10.8a15 15 0 0 0 6.6 6.6l2.2-2.2a1 1 0 0 1 1-.25 11.4 11.4 0 0 0 3.6.6 1 1 0 0 1 1 1V20a1 1 0 0 1-1 1A17 17 0 0 1 3 4a1 1 0 0 1 1-1h3.5a1 1 0 0 1 1 1c0 1.25.2 2.45.6 3.6a1 1 0 0 1-.25 1z"/></svg>
        509 555 0182
      </p>
      <p class="contact-line">
        <svg viewBox="0 0 24 24" aria-hidden="true"><rect x="2.5" y="5" width="19" height="14" rx="1.5" fill="none" stroke="currentColor" stroke-width="2"/><path d="M3 6l9 7 9-7" fill="none" stroke="currentColor" stroke-width="2"/></svg>
        info@silverheron.com
      </p>
      <p class="contact-line">
        <svg viewBox="0 0 24 24" aria-hidden="true"><g fill="none" stroke="currentColor" stroke-width="2"><circle cx="12" cy="12" r="9.5"/><ellipse cx="12" cy="12" rx="4.2" ry="9.5"/><path d="M2.5 12h19M4 7h16M4 17h16"/></g></svg>
        www.silverheron.com
      </p>
    </div>
  </section>

</main>
</body>
</html>
```